WordPress Website for Pain Relief Clinic

I need a WordPress website designed for my laser pain relief clinic. It needs to be a professional, responsive design with 7 pages: Home, Why Choose Us, Treatable Conditions, Testimonials, FAQ, Franchising, Contact Us. Here is logo: https://files.brivoltcdn.com/media.t-w-e-n.com/sitebuilder/472/CalvexaLogoHighQuality.png

Target Market(s)

people with pain,elderly adults,injuries,soreness

Industry/Entity Type

Clinic

Number of Pages Required

5+ page

Colors
0792cd
85abd2

```html
<!DOCTYPE html>
<html lang="en">
<head>
<meta charset="utf-8">
<title>Calvexa Pain Treatment Center</title>
<link href="https://fonts.googleapis.com/css2?family=Open+Sans:wght@400;600;700&family=Oswald:wght@400;500&display=swap" rel="stylesheet">
<style>
:root{
  --blue:#0792cd;
  --blue-dark:#0a6fa3;
  --blue-soft:#85abd2;
  --red:#d8232a;
  --ink:#333;
  --muted:#777;
  --line:#dcdcdc;
  --page:#eef0f2;
  --dark:#2e3134;
  --darker:#222426;
}
*{box-sizing:border-box;margin:0;padding:0}
html,body{width:756px;height:1200px;overflow:hidden}
body{background:var(--page);font-family:'Open Sans',Arial,sans-serif;color:var(--ink);font-size:9px;line-height:1.45}
.site{width:756px;height:1200px;position:relative;background:#fff}
/* header */
.header{height:80px;display:flex;align-items:center;justify-content:space-between;padding:0 34px}
.brand{display:flex;align-items:center;gap:8px}
.brand-mark{width:16px;height:16px;background:var(--red)}
.brand-name{font-size:30px;font-weight:700;color:var(--blue-dark);letter-spacing:-.5px;line-height:1}
.brand-tag{font-size:7px;color:var(--muted);letter-spacing:2px;margin-top:2px}
.header-cta{text-align:right}
.call{display:flex;align-items:center;gap:6px;justify-content:flex-end}
.call small{display:block;font-size:7px;color:var(--muted)}
.call strong{font-size:15px;color:var(--ink)}
.appt{display:inline-block;margin-top:6px;background:var(--red);color:#fff;font-weight:700;font-size:8px;padding:6px 12px}
/* nav */
.nav{height:24px;background:linear-gradient(#1a9fd8,var(--blue-dark));display:flex;padding:0 34px}
.nav a{color:#fff;text-decoration:none;font-size:7.5px;font-weight:700;padding:0 11px;line-height:24px}
.nav a.active{background:var(--blue-soft)}
/* hero */
.hero{height:270px;position:relative;background:linear-gradient(90deg,#dfe6ec 0%,#c9d6e2 45%,#1f6fa7 60%,#0b4f86 100%);overflow:hidden}
.hero-photo{position:absolute;left:0;top:0;width:430px;height:270px;background:linear-gradient(120deg,#f0f2f4 0%,#d6b39a 40%,#c99b80 60%,#e8ecef 100%)}
.hero-copy{position:absolute;left:455px;top:75px;width:260px;color:#fff}
.hero-copy h1{font-family:'Oswald',sans-serif;font-weight:400;font-size:26px;letter-spacing:.5px}
.hero-copy p{font-size:8px;opacity:.85;margin:4px 0 14px}
.hero-phone{display:inline-flex;align-items:center;gap:8px;background:#111;padding:8px 12px;font-size:17px;font-weight:700}
/* tabs */
.tabs{height:34px;background:linear-gradient(#55595c,#3a3d40);display:flex;padding:0 34px;gap:2px}
.tab{display:flex;align-items:center;gap:7px;color:#fff;font-weight:700;font-size:10px;padding:0 22px}
.tab.on{background:var(--blue)}
.tab i{width:16px;height:16px;border:2px solid #fff;border-radius:50%}
/* service cards */
.services{background:linear-gradient(#dbe6f0,#f4f7fa);padding:12px 34px 18px;display:flex;gap:12px}
.card{flex:1;background:#fff;border:1px solid var(--line)}
.card h3{background:var(--blue);color:#fff;font-family:'Oswald',sans-serif;font-weight:500;font-size:13px;padding:4px 10px}
.card-photo{height:72px;margin:6px 8px;background:linear-gradient(135deg,#e9d2c3,#c89a82)}
.card p{padding:0 10px;font-size:7.5px;color:var(--muted)}
.more{display:block;text-align:right;font-size:7px;color:var(--blue);padding:4px 10px 8px}
/* welcome */
.intro{display:flex;gap:24px;padding:16px 34px;height:152px}
.welcome{flex:1.6}
h2{font-size:15px;font-weight:600;color:var(--ink);margin-bottom:6px}
h2 span{color:var(--blue)}
.welcome p{font-size:7.5px;color:var(--muted);margin-bottom:6px}
.welcome .lead{color:var(--ink);font-weight:600}
.health{flex:1}
.health li{list-style:none;padding-left:14px;position:relative;font-size:7.5px;color:var(--muted);margin-bottom:6px}
.health li::before{content:"";position:absolute;left:0;top:3px;width:6px;height:6px;background:var(--blue);border-radius:50%}
.health li b{color:var(--ink);display:block}
/* feature boxes */
.features{display:flex;gap:12px;padding:6px 34px 22px}
.box{flex:1;border:1px solid var(--line);background:#fff;height:186px}
.box h3{font-size:12px;font-weight:600;padding:8px 10px;border-bottom:1px solid var(--line)}
.box h3 span{color:var(--blue)}
.box-photo{height:58px;margin:8px 10px;background:linear-gradient(135deg,#dfe8ef,#9bb8cf)}
.box p{padding:0 10px;font-size:7.5px;color:var(--muted)}
.form{padding:8px 10px}
.form div{height:16px;border:1px solid var(--line);margin-bottom:6px;font-size:7px;color:#999;padding:2px 5px}
.form .msg{height:44px}
.form .send{display:inline-block;background:var(--blue);color:#fff;font-size:7px;font-weight:700;padding:4px 10px}
/* footer */
.footer{background:var(--dark);height:150px;padding:20px 34px;display:flex;gap:30px;color:#ccc}
.footer h4{color:#fff;font-size:10px;font-weight:600;margin-bottom:8px}
.links{display:grid;grid-template-columns:repeat(2,90px);gap:5px;font-size:7.5px}
.links span::before{content:"› ";color:var(--blue)}
.contact p{font-size:7.5px;margin-bottom:5px}
.foot-brand{margin-left:auto;align-self:center;font-size:30px;font-weight:700;color:#d6d9dc}
.copy{background:var(--darker);color:#999;font-size:7px;text-align:center;height:40px;line-height:40px}
</style>
</head>
<body>
<div class="site">
  <header class="header">
    <div class="brand">
      <div>
        <div class="brand-name">Calvexa</div>
        <div class="brand-tag">PAIN TREATMENT CENTER</div>
      </div>
    </div>
    <div class="header-cta">
      <div class="call">
        <svg width="16" height="16" viewBox="0 0 24 24"><path fill="#0792cd" d="M6.6 10.8a15 15 0 0 0 6.6 6.6l2.2-2.2c.3-.3.7-.4 1-.2 1.1.4 2.3.6 3.6.6.6 0 1 .4 1 1V20c0 .6-.4 1-1 1A17 17 0 0 1 3 4c0-.6.4-1 1-1h3.5c.6 0 1 .4 1 1 0 1.3.2 2.5.6 3.6.1.3 0 .7-.2 1z"/></svg>
        <div><small>Call Us Today</small><strong>555-201-4480</strong></div>
      </div>
      <span class="appt">MAKE AN APPOINTMENT</span>
    </div>
  </header>

  <nav class="nav">
    <a class="active">HOME</a><a>WHY CHOOSE US</a><a>TREATABLE CONDITIONS</a><a>TESTIMONIALS</a><a>FAQ</a><a>FRANCHISING</a><a>CONTACT US</a>
  </nav>

  <section class="hero">
    <div class="hero-photo" role="img" aria-label="Photo of a clinician applying laser therapy to a patient's shoulder"></div>
    <div class="hero-copy">
      <h1>CARE WITHOUT BORDERS</h1>
      <p>Gentle laser therapy that eases chronic pain and helps you move freely again, without drugs or surgery.</p>
      <div class="hero-phone">
        <svg width="14" height="14" viewBox="0 0 24 24"><path fill="#fff" d="M6.6 10.8a15 15 0 0 0 6.6 6.6l2.2-2.2c.3-.3.7-.4 1-.2 1.1.4 2.3.6 3.6.6.6 0 1 .4 1 1V20c0 .6-.4 1-1 1A17 17 0 0 1 3 4c0-.6.4-1 1-1h3.5c.6 0 1 .4 1 1 0 1.3.2 2.5.6 3.6.1.3 0 .7-.2 1z"/></svg>
        555-201-4480
      </div>
    </div>
  </section>

  <div class="tabs">
    <div class="tab on"><i></i>SOLUTIONS</div>
    <div class="tab"><i></i>WHY US?</div>
    <div class="tab"><i></i>TESTIMONIAL</div>
    <div class="tab"><i></i>CONTACT US</div>
  </div>

  <section class="services">
    <article class="card">
      <h3>BACK PAIN</h3>
      <div class="card-photo" role="img" aria-label="Photo of a person holding their lower back"></div>
      <p>Targeted laser sessions reduce swelling and stiffness in the lower back so daily tasks feel easier.</p>
      <span class="more">» Read More</span>
    </article>
    <article class="card">
      <h3>KNEE PAIN</h3>
      <div class="card-photo" role="img" aria-label="Photo of a knee with a highlighted area of pain"></div>
      <p>Relief for worn joints and sports injuries, helping you walk, climb and kneel with comfort.</p>
      <span class="more">» Read More</span>
    </article>
    <article class="card">
      <h3>SHOULDER PAIN</h3>
      <div class="card-photo" role="img" aria-label="Photo of a person holding a sore shoulder"></div>
      <p>Calm inflamed tendons and restore range of motion after strain, overuse or minor injury.</p>
      <span class="more">» Read More</span>
    </article>
  </section>

  <section class="intro">
    <div class="welcome">
      <h2>Welcome to <span>Calvexa</span></h2>
      <p class="lead">Our clinic offers safe, non-invasive laser treatment for lasting pain relief at every stage of life.</p>
      <p>We work with older adults, athletes and anyone living with soreness or injury. Each plan is built around your needs, your goals and your pace, with gentle care from a friendly team.</p>
      <p>Sessions are short and comfortable, and most patients notice change within a few visits. Book a free consultation to learn how laser care can help you feel like yourself again.</p>
      <span class="more" style="padding:0">Read more »</span>
    </div>
    <aside class="health">
      <h2>Health <span>Information</span></h2>
      <ul>
        <li><b>How laser therapy works</b>Light energy helps damaged cells heal faster.</li>
        <li><b>Tips for joint health</b>Simple daily habits that keep you moving.</li>
        <li><b>Recovering from injury</b>What to expect during your treatment plan.</li>
      </ul>
    </aside>
  </section>

  <section class="features">
    <div class="box">
      <h3><span>Why</span> Choose Us</h3>
      <div class="box-photo" role="img" aria-label="Photo of the clinic's medical team"></div>
      <p>Trained staff, proven methods and caring service in a calm, modern clinic.</p>
      <span class="more">Read more »</span>
    </div>
    <div class="box">
      <h3><span>How</span> Does it Work</h3>
      <div class="box-photo" role="img" aria-label="Photo of a doctor explaining treatment"></div>
      <p>A quick assessment, a tailored plan, then short painless laser sessions.</p>
      <span class="more">Read more »</span>
    </div>
    <div class="box">
      <h3>Quick Contact</h3>
      <div class="form">
        <div>Name</div>
        <div>Email</div>
        <div class="msg">Message</div>
        <span class="send">SUBMIT</span>
      </div>
    </div>
  </section>

  <footer class="footer">
    <div>
      <h4>Links</h4>
      <div class="links">
        <span>Home</span><span>Testimonials</span>
        <span>Why Choose Us</span><span>Franchising</span>
        <span>Treatable Conditions</span><span>Contact Us</span>
        <span>FAQ</span>
      </div>
    </div>
    <div class="contact">
      <h4>Contact Us</h4>
      <p>1200 Harbor Lane, Suite 4, Springfield</p>
      <p>555-201-4480</p>
      <p>hello@calvexaclinic.com</p>
    </div>
    <div class="foot-brand">Calvexa</div>
  </footer>
  <div class="copy">Copyright © 2024 Calvexa. All Rights Reserved.</div>
</div>
</body>
</html>
```